Havenmark Electrical Business Card

create a simple but clear business card and letterhead - needs to be professional not too fancy and direct.

Target Market(s)

Home builders

Contact Information for Business Card

Information needed
Havenmark Electrical Contracting
EC. No. 418237
Derek Hollowell
Mobile 0437215609
derek@havenmarkelectrical.com.au

Requirements
Must have
• logo
• Havenmark Electrical Contracting - H.E.C.
• EC. No. 418237
• Derek Hollowell
• Mobile 0437215609
• derek@havenmarkelectrical.com.au
Nice to have
• black with white printing simple but clear
Should not have
• too much information
• no fancy writing

```html
<!DOCTYPE html>
<html lang="en">
<head>
<meta charset="utf-8">
<title>Havenmark Electrical Business Card</title>
<link href="https://fonts.googleapis.com/css2?family=Lato:wght@400;700;900&display=swap" rel="stylesheet">
<style>
  :root {
    --backdrop: #e4e4e4;
    --card-dark: #2b2b2b;
    --card-light: #ffffff;
    --swoosh: #c4c4c4;
    --ink-light: #ffffff;
    --ink-dark: #262626;
    --ink-soft: #e8e8e8;
  }
  * { margin: 0; padding: 0; box-sizing: border-box; }
  html, body {
    width: 1200px; height: 900px; overflow: hidden;
    background: var(--backdrop);
    font-family: "Lato", Arial, sans-serif;
  }
  .sheet {
    width: 1200px; height: 900px;
    display: flex; flex-direction: column; align-items: center; justify-content: center;
    gap: 60px;
  }
  .card {
    position: relative;
    width: 580px; height: 350px;
    overflow: hidden;
    box-shadow: 0 10px 28px rgba(0,0,0,0.22);
  }
  .card--back { background: var(--card-dark); }
  .card--front { background: var(--card-light); }
  .card__shape { position: absolute; inset: 0; width: 100%; height: 100%; }

  .brand {
    position: absolute;
    display: flex; align-items: center; gap: 16px;
    font-weight: 900;
    line-height: 1.05;
  }
  .brand__dot {
    width: 64px; height: 64px; border-radius: 50%;
    flex: none;
  }
  .brand__name { font-size: 30px; letter-spacing: 0.5px; }
  .brand__name span { display: block; font-size: 19px; letter-spacing: 0.3px; }

  .card--back .brand { left: 150px; top: 132px; color: var(--ink-light); }
  .card--back .brand__dot { background: var(--ink-light); }

  .card--front .brand { left: 70px; top: 38px; color: var(--ink-dark); }
  .card--front .brand__dot { background: var(--ink-dark); }

  .contact {
    position: absolute; left: 34px; top: 196px;
    color: var(--ink-soft);
  }
  .contact__name { font-size: 21px; font-weight: 400; margin-bottom: 8px; color: var(--ink-light); }
  .contact__company { font-size: 14px; margin-bottom: 3px; padding-left: 4px; }
  .contact__line { font-size: 14px; display: flex; align-items: center; gap: 8px; margin-bottom: 2px; }
  .contact__line svg { width: 12px; height: 12px; flex: none; }
  .licence {
    position: absolute; right: 34px; bottom: 22px;
    font-size: 17px; color: var(--ink-light); letter-spacing: 0.5px;
  }
</style>
</head>
<body>
<main class="sheet">
  <section class="card card--back" aria-label="Business card back">
    <div class="brand">
      <div class="brand__dot"></div>
      <div class="brand__name">HAVENMARK<span>Electrical Contracting</span></div>
    </div>
  </section>

  <section class="card card--front" aria-label="Business card front">
    <svg class="card__shape" viewBox="0 0 580 350" preserveAspectRatio="none" aria-hidden="true">
      <path d="M0 148 C 160 150, 380 175, 580 262 L580 350 L0 350 Z" fill="var(--swoosh)"/>
      <path d="M0 164 C 170 168, 390 195, 580 282 L580 350 L0 350 Z" fill="var(--card-dark)"/>
    </svg>
    <div class="brand">
      <div class="brand__dot"></div>
      <div class="brand__name">HAVENMARK<span>Electrical Contracting</span></div>
    </div>
    <div class="contact">
      <p class="contact__name">Derek Hollowell</p>
      <p class="contact__company">Havenmark Electrical Contracting</p>
      <p class="contact__line">
        <svg viewBox="0 0 12 12"><rect x="3" y="0.5" width="6" height="11" rx="1" fill="none" stroke="currentColor"/><rect x="4.2" y="2" width="3.6" height="6" fill="currentColor"/></svg>
        0437 215609
      </p>
      <p class="contact__line">
        <svg viewBox="0 0 12 12"><rect x="0.5" y="2" width="11" height="8" fill="none" stroke="currentColor"/><path d="M0.5 2 L6 7 L11.5 2" fill="none" stroke="currentColor"/></svg>
        derek@havenmarkelectrical.com.au
      </p>
    </div>
    <p class="licence">EC. No. 418237</p>
  </section>
</main>
</body>
</html>
```